Serenelle Aura Candle Box Package Design

Two box sizes:
14oz Candle in a box Gift Boxes - 4 x 4 x 6
4oz Candle in a box Gift Boxes - 3 x 3 x 3
Website: www.serenelleaura.com
IG: @serenelle.aura
My brand is a sophisticated brand with luxury candles made of coconut wax.  Serenelle Aura means bright life. Our candles represent hope and light.
You matter, you are worthy, powerful and beautiful!
Each candle is hand poured, vegan, environmentally conscious, uniquely scented and rooted in the importance of self care and community. We donate a percentage of our proceeds to organizations that seek to empower and enrich women.
At Serenelle Aura, we believe that positive energy can move mountains.
We strive to elevate that energy in every way possible. Our candles are handmade with confident positivity in mind - 100% vegan friendly, non-toxic and carefully crafted for optimal performance yet minimal impact on the environment.

```html
<!DOCTYPE html>
<html lang="en">
<head>
<meta charset="utf-8">
<title>Serenelle Aura – Candle Box Panels</title>
<link rel="stylesheet" href="https://fonts.googleapis.com/css2?family=Cormorant+Garamond:wght@300;400;600;700&family=Montserrat:wght@300&display=swap">
<style>
  :root {
    --page: #efeceb;
    --panel: #ffffff;
    --blush: #f6cfc6;
    --blush-soft: #fbe6e1;
    --rose-text: #e8a8a0;
    --rose-deep: #d98c84;
    --gold: #e9d27a;
    --ink: #3a2d2b;
    --badge: #b88a72;
  }
  * { box-sizing: border-box; margin: 0; padding: 0; }
  html, body { width: 1200px; height: 900px; overflow: hidden; background: var(--page); }
  .stage { position: relative; width: 1200px; height: 900px; }

  .box-panel {
    position: absolute; top: 135px; width: 420px; height: 630px;
    background: var(--panel); overflow: hidden;
    box-shadow: 0 10px 30px rgba(90, 60, 50, 0.12);
  }
  .box-panel--front { left: 140px; }
  .box-panel--back { left: 640px; }

  .watercolor {
    position: absolute; pointer-events: none;
  }
  .watercolor--top {
    top: 0; left: 0; width: 100%; height: 300px;
    background:
      radial-gradient(ellipse 60% 55% at 78% 20%, var(--blush) 0%, rgba(246,207,198,0) 70%),
      radial-gradient(ellipse 45% 50% at 10% 25%, var(--blush-soft) 0%, rgba(251,230,225,0) 75%),
      radial-gradient(ellipse 30% 20% at 55% 45%, rgba(233,210,122,0.35) 0%, rgba(233,210,122,0) 80%);
  }
  .box-panel--back .watercolor--top {
    background:
      radial-gradient(ellipse 70% 60% at 30% 25%, var(--blush) 0%, rgba(246,207,198,0) 72%),
      radial-gradient(ellipse 50% 50% at 88% 20%, var(--blush) 0%, rgba(246,207,198,0) 75%),
      radial-gradient(ellipse 35% 20% at 55% 40%, rgba(233,210,122,0.35) 0%, rgba(233,210,122,0) 80%);
  }
  .watercolor--bottom {
    bottom: 0; left: 0; width: 100%; height: 220px;
    background:
      radial-gradient(ellipse 30% 45% at 5% 70%, var(--blush-soft) 0%, rgba(251,230,225,0) 75%),
      radial-gradient(ellipse 25% 35% at 95% 70%, var(--blush-soft) 0%, rgba(251,230,225,0) 75%),
      radial-gradient(ellipse 20% 15% at 40% 85%, rgba(233,210,122,0.3) 0%, rgba(233,210,122,0) 80%);
  }

  .seal {
    position: absolute; top: 40px; left: 30px; width: 64px; height: 64px;
    border-radius: 50%; border: 2px solid var(--rose-deep); background: #fff5f3;
  }

  .brand-block {
    position: absolute; top: 265px; left: 0; width: 100%; text-align: center;
  }
  .brand-name {
    font-family: "Cormorant Garamond", serif; font-weight: 300;
    font-size: 44px; letter-spacing: 1px; color: var(--rose-text); line-height: 1;
  }
  .brand-sub {
    margin-top: 20px; display: flex; align-items: center; justify-content: center; gap: 12px;
    font-family: "Montserrat", sans-serif; font-weight: 300; font-size: 12px;
    letter-spacing: 7px; color: var(--rose-text);
  }
  .brand-sub::before, .brand-sub::after {
    content: ""; width: 24px; height: 1px; background: var(--rose-text);
  }
  .brand-tagline {
    margin: 18px auto 0; width: 130px; height: 16px; border-radius: 8px;
    background: linear-gradient(90deg, rgba(246,207,198,0), var(--blush-soft), rgba(246,207,198,0));
  }
  .portrait-line-art {
    position: absolute; left: 175px; top: 410px; width: 160px; height: 190px;
    border-radius: 45% 45% 40% 40%;
    background: radial-gradient(ellipse at 50% 45%, rgba(246,207,198,0.45) 0%, rgba(246,207,198,0.1) 70%, rgba(246,207,198,0) 100%);
  }

  .brand-story {
    position: absolute; top: 70px; left: 48px; right: 48px;
    font-family: "Cormorant Garamond", serif; font-weight: 600;
    font-size: 10.6px; line-height: 1.27; color: var(--rose-deep); text-align: justify;
  }
  .brand-story h3 {
    font-weight: 700; font-size: 11.5px; color: var(--ink); margin-top: 2px; text-align: left;
  }
  .brand-story p { margin: 0; }

  .feature-badges {
    position: absolute; bottom: 48px; left: 40px; right: 40px;
    display: flex; justify-content: space-between;
  }
  .feature-badge {
    width: 38px; height: 38px; border-radius: 50%;
    border: 1px solid var(--badge); background: rgba(255,255,255,0.8);
    display: flex; align-items: center; justify-content: center; text-align: center;
    font-family: "Cormorant Garamond", serif; font-weight: 600; font-size: 6.5px;
    line-height: 1.1; color: var(--badge);
  }
  .feature-badge span { display: block; width: 30px; }
</style>
</head>
<body>
<main class="stage">

  <section class="box-panel box-panel--front" aria-label="Front panel">
    <div class="watercolor watercolor--top" role="img" aria-label="Blush watercolour wash with gold marbling veins and splatter"></div>
    <div class="watercolor watercolor--bottom" role="img" aria-label="Soft blush watercolour corners with gold dots"></div>
    <div class="seal" role="img" aria-label="Handmade badge"></div>
    <div class="brand-block">
      <h1 class="brand-name">SERENELLE AURA</h1>
      <p class="brand-sub">HANDMADE CANDLES</p>
      <div class="brand-tagline" role="img" aria-label="Hand-lettered tagline: with purpose and love"></div>
    </div>
    <div class="portrait-line-art" role="img" aria-label="Fine blush line illustration of a classical figure in profile"></div>
  </section>

  <section class="box-panel box-panel--back" aria-label="Back panel">
    <div class="watercolor watercolor--top" role="img" aria-label="Blush watercolour wash with gold marbling veins and splatter"></div>
    <div class="watercolor watercolor--bottom" role="img" aria-label="Soft blush watercolour corners with gold dots"></div>
    <div class="brand-story">
      <p>Serenelle Aura means bright life. Our candles represent hope and light.<br>
      You matter, you are worthy, powerful and beautiful!<br>
      Each candle is hand poured, vegan, environmentally conscious, uniquely scented and rooted in the importance of self care and community. We donate a percentage of our proceeds to organizations that seek to empower and enrich women.</p>
      <h3>Our beliefs</h3>
      <p>In helping yourself, you are also helping others.<br>
      Being your best self and lighting the way for others in your community and beyond is how we all win. We make luxury candles with intention to help you relax and cultivate a space of peace, while disrupting big candle businesses that value quantity over quality and environment.</p>
      <h3>Empowerment</h3>
      <p>We believe in empowering women to embrace their true potential, creating an uplifting environment where they can flourish and inspire others. Our candles are crafted to ignite a sense of confidence and motivation, encouraging personal growth and inner strength.</p>
      <h3>Honesty</h3>
      <p>Transparency is at the heart of our brand. We value open and authentic communication, ensuring that our customers have access to accurate information about our products and processes. With every Serenelle Aura candle, you can trust that what you see is what you get – pure, non-toxic ingredients and a commitment to integrity.</p>
      <h3>Respect</h3>
      <p>We honor diversity and inclusivity in all aspects of our brand. We respect every individual's unique journey and provide a safe space for self-expression. Our candles are designed to create a calming ambiance that fosters harmony and acceptance, allowing everyone to feel valued and appreciated.</p>
      <h3>Sustainability</h3>
      <p>We are intentional in the crafting of our goods. We utilize a vegan blend of natural coconut wax. Our candles provide a clean and slow burn, creamy and luxurious texture, and a strong scent. They are natural, non-toxic, skin-safe, and pet friendly.</p>
    </div>
    <ul class="feature-badges" aria-label="Product features">
      <li class="feature-badge"><span>Non Toxic</span></li>
      <li class="feature-badge"><span>Long Lasting</span></li>
      <li class="feature-badge"><span>Smokeless</span></li>
      <li class="feature-badge"><span>Eco Friendly</span></li>
      <li class="feature-badge"><span>Phthalate Free</span></li>
      <li class="feature-badge"><span>Vegan</span></li>
      <li class="feature-badge"><span>100% Coconut Wax</span></li>
      <li class="feature-badge"><span>Cruelty Free</span></li>
    </ul>
  </section>

</main>
</body>
</html>
```